KV HOLDINGS Business Cards

I need business cards for "KV Holdings group LLC" doublesided... logo on the back (also include logo on front)
logo attached to project... i have jpg up..
Company Info:
418 North Palmer Avenue, Suite 7B
Chicago, Illinois 60654
facsimile 312-555-0187 (list fax, address, website on all cards.)
www.kvholdingsgroup.example
Three different people on cards:
Darnell P. Okafor, CPA MST
Principal
ofc 312-555-0142
mobile 312-555-0169
darnellpokafor@kvholdingsgroup.example
Gregor T. Vanhoutte, CPA MST
Principal
gregortvanhoutte@kvholdingsgroup.example
mobile 708-555-0113
ofc 312-555-0142
Tobias M Quarrie
Principal
ofc 312-555-0142
no mobile
tobiasmquarrie@kvholdingsgroup.example
I have multiple projects listed.. see below:
Business cards for amber ledge partners llc
letterhead
envelopes
Business cards for KV Holdings LLC
letterhead
envelopes
Target Market(s)
rich people
Industry/Entity Type
Business

```html
<!DOCTYPE html>
<html lang="en">
<head>
<meta charset="utf-8">
<title>KV Holdings Group LLC – Business Card</title>
<link rel="stylesheet" href="https://fonts.googleapis.com/css2?family=Fira+Sans:wght@400;500&display=swap">
<style>
  :root {
    --blue-base: #0b52e6;
    --blue-light: #2a7ef5;
    --blue-deep: #0a2f9e;
    --blue-brand: #1c3c9c;
    --white: #ffffff;
    --text-light: #f2f6ff;
  }
  html, body {
    margin: 0;
    padding: 0;
    width: 1200px;
    height: 777px;
    overflow: hidden;
    background: var(--blue-base);
  }
  .card {
    position: relative;
    width: 1200px;
    height: 777px;
    overflow: hidden;
    font-family: "Fira Sans", sans-serif;
  }
  .card-background {
    position: absolute;
    inset: 0;
  }
  .brand-name {
    position: absolute;
    left: 0;
    width: 1200px;
    top: 260px;
    text-align: center;
    margin: 0;
    font-family: "Fira Sans", sans-serif;
    font-weight: 500;
    font-size: 32px;
    line-height: 40px;
    letter-spacing: 1px;
    color: var(--blue-brand);
  }
  .contact {
    position: absolute;
    margin: 0;
    color: var(--text-light);
    font-size: 24px;
    line-height: 30px;
    font-weight: 400;
  }
  .contact p { margin: 0; white-space: nowrap; }
  .contact-person { left: 180px; top: 455px; }
  .contact-company { left: 688px; top: 469px; }
  .divider {
    position: absolute;
    left: 660px;
    top: 466px;
    width: 2px;
    height: 132px;
    background: var(--white);
  }
</style>
</head>
<body>
<main class="card">
  <svg class="card-background" width="1200" height="777" viewBox="0 0 1200 777" aria-hidden="true">
    <defs>
      <radialGradient id="glow" cx="0.48" cy="0.55" r="0.65">
        <stop offset="0" stop-color="#1f72f6"/>
        <stop offset="0.6" stop-color="#0b52e6"/>
        <stop offset="1" stop-color="#0a38b8"/>
      </radialGradient>
    </defs>
    <rect width="1200" height="777" fill="url(#glow)"/>
    <polygon points="0,0 300,0 330,777 0,777" fill="var(--blue-light)" opacity="0.25"/>
    <polygon points="0,380 180,777 0,777" fill="var(--blue-deep)" opacity="0.35"/>
    <polygon points="900,0 1200,0 1200,777 1080,777 820,320" fill="var(--blue-deep)" opacity="0.55"/>
    <polygon points="820,320 1080,777 900,777 700,420" fill="var(--blue-deep)" opacity="0.3"/>
    <polygon points="620,0 900,0 760,240" fill="var(--blue-light)" opacity="0.2"/>
    <ellipse cx="600" cy="227" rx="680" ry="104" fill="var(--white)"/>
  </svg>

  <p class="brand-name">KV Holdings Group LLC</p>

  <section class="contact contact-person">
    <p class="person-name">Tobias M Quarrie</p>
    <p class="person-title">Principal</p>
    <p>ofc 312-555-0142</p>
    <p>no mobile</p>
    <p>tobiasmquarrie@kvholdingsgroup.example</p>
  </section>

  <div class="divider"></div>

  <section class="contact contact-company">
    <p>418 North Palmer Avenue, Suite 7B</p>
    <p>Chicago, Illinois 60654</p>
    <p>facsimile 312-555-0187</p>
    <p>www.kvholdingsgroup.example</p>
  </section>
</main>
</body>
</html>
```